Business Card Design for N orthern M eadow H abitat P roject

business card for non-profit
-use logo uploaded (thanks artist brelquon)
-include n m h p. o r g website and include the three names - titles - emails from website
-recognize sponsors on the card somehow. logos or names?
Quellmark Horticultural Grounds Association, Fernholt Bloom Society of QZ and Ostrava Greenway Foundation

-include colony of1) Trillium ovatum on the card or maybe Erythronium revolutum
or 2) just keep it simple with the logo

-single sided card is fine but I am posting double sided as an option as I am guessing that all this writing may require two sides.

Target Market(s)
-people who have plants and or time to contribute

Business Card Design Requirements
Must Have:
- Project Name
- Contact info
- Website

Industry/Entity Type

Business

Requirements
Must have
• All four contacts on the card please,
• Meadow Habitat Project Coordinator - Tobias - northernmeadow@ postvelt.com
• Nursery Operations Coordinator - Milo - nursery.nmhp@ postvelt.com
• Seed Collection Coordinator - Milo - seeds.nmhp@postvelt.com
• Plant Rescue Operations Coordinator- Greta - plantrescue.nmhp@ postvelt.com

```html
<!DOCTYPE html>
<html lang="en">
<head>
<meta charset="utf-8">
<title>Northern Meadow Habitat Project – Business Card</title>
<link rel="stylesheet" href="https://fonts.googleapis.com/css2?family=Questrial&family=Mulish:wght@700;800&display=swap">
<style>
  :root {
    --bg: #2a2a2a;
    --paper: #f4f4f3;
    --paper-raised: #fbfbfa;
    --ink: #3a3a3a;
    --ink-strong: #1f1f1f;
    --leaf: #5cbf3a;
    --leaf-deep: #2f6b2a;
    --sun: #f2e61c;
    --foliage-dark: #1f3a1c;
    --foliage-mid: #4f7a3c;
    --foliage-light: #9fbf86;
    --veil: rgba(255,255,255,0.62);
  }
  * { box-sizing: border-box; margin: 0; padding: 0; }
  html, body { width: 1200px; height: 660px; overflow: hidden; }
  body {
    background: var(--bg);
    font-family: "Questrial", "Helvetica Neue", Arial, sans-serif;
    position: relative;
  }
  .card {
    position: absolute;
    top: 175px;
    width: 540px;
    height: 310px;
    overflow: hidden;
    box-shadow: 0 12px 28px rgba(0,0,0,0.45);
  }
  .card--front { left: 45px; }
  .card--back { left: 615px; background: var(--paper); }

  /* Front */
  .front-photo {
    position: absolute; inset: 0;
    background:
      radial-gradient(ellipse at 25% 20%, var(--foliage-light) 0%, transparent 45%),
      radial-gradient(ellipse at 80% 85%, var(--foliage-mid) 0%, transparent 55%),
      linear-gradient(160deg, var(--foliage-dark) 0%, var(--foliage-mid) 50%, var(--foliage-dark) 100%);
  }
  .front-band {
    position: absolute; left: 0; right: 0; top: 78px; height: 130px;
    background: var(--veil);
    border-top: 3px solid var(--leaf);
    border-bottom: 3px solid var(--leaf);
    box-shadow: 0 -4px 0 var(--sun), 0 4px 0 var(--sun);
    display: flex; align-items: center; justify-content: center;
  }
  .front-web {
    position: absolute; left: 0; right: 0; bottom: 58px;
    text-align: center;
    font-family: "Mulish", Arial, sans-serif; font-weight: 800;
    color: #fff; font-size: 17px; letter-spacing: 0.3px;
  }

  /* Name lockup */
  .lockup { display: flex; align-items: center; gap: 10px; }
  .lockup-dot {
    width: 22px; height: 22px; border-radius: 50%;
    background: var(--leaf); flex: none;
  }
  .lockup-name {
    font-family: "Questrial", Arial, sans-serif;
    color: var(--ink-strong); font-size: 19px; line-height: 1.15;
  }

  /* Back */
  .back-top {
    position: absolute; left: 0; right: 0; top: 0; height: 14px;
    background: var(--sun); border-bottom: 3px solid var(--leaf);
  }
  .back-bottom {
    position: absolute; left: 0; right: 0; bottom: 0; height: 16px;
    background: var(--leaf); border-top: 3px solid var(--sun);
  }
  .back-logo {
    position: absolute; left: 26px; top: 100px; width: 200px;
  }
  .back-logo .lockup-name { font-size: 18px; }
  .contact-panel {
    position: absolute; right: 0; top: 17px; bottom: 19px; width: 300px;
    background: var(--paper-raised);
    box-shadow: -4px 0 8px rgba(0,0,0,0.08);
    padding: 34px 18px 0 26px;
  }
  .contact { margin-bottom: 14px; color: var(--ink); font-size: 12.5px; line-height: 1.35; }
  .contact-name { font-weight: 700; font-family: "Mulish", Arial, sans-serif; color: var(--ink-strong); }
</style>
</head>
<body>
  <section class="card card--front" aria-label="Card front">
    <div class="front-photo" role="img" aria-label="Photograph of a colony of white woodland lilies among green foliage"></div>
    <div class="front-band">
      <div class="lockup">
        <span class="lockup-dot"></span>
        <span class="lockup-name">Northern Meadow<br>Habitat Project</span>
      </div>
    </div>
    <p class="front-web">www.meadowhabitatnmhp.org</p>
  </section>

  <section class="card card--back" aria-label="Card back">
    <div class="back-top"></div>
    <div class="back-logo">
      <div class="lockup">
        <span class="lockup-dot"></span>
        <span class="lockup-name">Northern Meadow<br>Habitat Project</span>
      </div>
    </div>
    <div class="contact-panel">
      <p class="contact">Meadow Habitat Project Coordinator<br><span class="contact-name">Tobias</span> - northernmeadow@ postvelt.com</p>
      <p class="contact">Nursery Operations Coordinator<br><span class="contact-name">Milo</span> - nursery.nmhp@ postvelt.com</p>
      <p class="contact">Seed Collection Coordinator<br><span class="contact-name">Milo</span> - seeds.nmhp@postvelt.com</p>
      <p class="contact">Plant Rescue Operations Coordinator<br><span class="contact-name">Greta</span> - plantrescue.nmhp@ postvelt.com</p>
    </div>
    <div class="back-bottom"></div>
  </section>
</body>
</html>
```